Business Card Design

Please visit www.MarkDorsey.com to acquire information for business card.

Back Side of Card:
a lifetime of experience working for you.

With over 25 years in the construction industry, well over a decade as a licensed Subcontractor / General Contractor and nearly 10 years as a licensed Realtor, I have excelled and cultivated a working knowledge of how all the pieces fit together.

Here is a link to folder.
https://files.examplecloud.net/folderview?id=7Qk2mXrTpLw9zVbN4sHcDyUeFaGj&usp=sharing

Industry/Entity Type

Construction

Contact Information for Business Card

Company: Mark Dorsey, LLC.
Address: 31872 W. Cedar Hollow Blvd. Suite 207-418
Name: Mark Dorsey
Phone: (623) 587-2914
Web: www.MarkDorsey.com
Type of services offered: Architectural Design, 3D Models, Renderings & Animation - Construction Documents - Project Managment.

```html
<!DOCTYPE html>
<html lang="en">
<head>
<meta charset="utf-8">
<title>Mark Dorsey, LLC. — Business Card</title>
<link href="https://fonts.googleapis.com/css2?family=Open+Sans:wght@400;700&family=Questrial&display=swap" rel="stylesheet">
<style>
  :root {
    --page: #e9e7e4;
    --ink: #0f1011;
    --ink-soft: #1c1e20;
    --band: #2c2e31;
    --column: #17181a;
    --paper: #ffffff;
    --text-light: #f2f2f2;
    --text-muted: #9a9c9f;
  }
  * { box-sizing: border-box; margin: 0; padding: 0; }
  html, body { width: 1200px; height: 800px; overflow: hidden; }
  body { background: var(--page); position: relative; font-family: "Open Sans", Arial, sans-serif; }

  .card { position: absolute; box-shadow: 0 6px 18px rgba(0,0,0,.25); overflow: hidden; }

  /* Back side */
  .card-back {
    left: 120px; top: 102px; width: 340px; height: 595px;
    background: linear-gradient(160deg, var(--ink-soft) 0%, var(--ink) 70%);
  }
  .card-back .tag-column {
    position: absolute; left: 0; top: 150px; bottom: 0; width: 58px;
    background: var(--column);
    border-right: 1px solid #26282b;
  }
  .card-back .tagline {
    position: absolute; left: 14px; top: 180px;
    writing-mode: vertical-rl;
    font-family: "Questrial", "Century Gothic", sans-serif;
    font-size: 15px; letter-spacing: .6px; text-transform: uppercase;
    color: var(--text-muted);
  }
  .card-back .name-band {
    position: absolute; left: 0; right: 0; top: 92px; height: 58px;
    background: linear-gradient(90deg, var(--band), #3a3c40);
    display: flex; align-items: center; padding-left: 36px;
  }
  .card-back .company {
    font-family: "Questrial", "Century Gothic", sans-serif;
    font-size: 27px; color: var(--text-light); letter-spacing: .3px;
  }
  .card-back .services {
    position: absolute; left: 98px; top: 178px;
    writing-mode: vertical-rl;
    list-style: none;
    font-size: 17px; line-height: 34px; color: var(--text-light);
  }
  .card-back .services li::before { content: "•"; margin-bottom: 8px; display: inline-block; }

  /* Front side */
  .card-front {
    left: 510px; top: 228px; width: 595px; height: 340px;
    display: flex; background: var(--ink);
  }
  .card-front .brand-panel {
    width: 270px; background: var(--paper);
    display: flex; align-items: center; justify-content: center;
  }
  .card-front .brand-frame {
    width: 220px; height: 220px;
    border: 3px solid var(--ink);
    outline: 1px solid var(--ink); outline-offset: 6px;
    display: flex; align-items: center; justify-content: center;
  }
  .card-front .brand-name {
    font-family: "Open Sans", Arial, sans-serif;
    font-size: 19px; color: var(--ink);
  }
  .card-front .info-panel {
    flex: 1; padding: 34px 0 0 30px; color: var(--text-light);
    background: linear-gradient(160deg, #1a1b1d, var(--ink) 60%);
  }
  .person { font-size: 21px; font-weight: 700; letter-spacing: .5px; text-transform: uppercase; }
  .role { font-size: 14px; color: #d0d0d0; margin-bottom: 14px; }
  .contacts { list-style: none; font-size: 16px; line-height: 27px; }
  .contacts li { display: flex; align-items: center; gap: 10px; }
  .contacts svg { width: 15px; height: 15px; flex: none; }
  .address { margin-top: 22px; font-size: 16px; line-height: 24px; font-style: normal; }
</style>
</head>
<body>
  <section class="card card-back" aria-label="Card back">
    <div class="tag-column"></div>
    <p class="tagline">A lifetime of experience working for you</p>
    <div class="name-band"><h2 class="company">Mark Dorsey, LLC.</h2></div>
    <ul class="services">
      <li>Architectural Design</li>
      <li>3D Models</li>
      <li>Renderings &amp; Animation</li>
      <li>Construction Documents</li>
      <li>Project Managment</li>
    </ul>
  </section>

  <section class="card card-front" aria-label="Card front">
    <div class="brand-panel">
      <div class="brand-frame"><span class="brand-name">Mark Dorsey, LLC.</span></div>
    </div>
    <div class="info-panel">
      <h1 class="person">Mark Dorsey</h1>
      <p class="role">Director</p>
      <ul class="contacts">
        <li>
          <svg viewBox="0 0 16 16" aria-hidden="true"><rect width="16" height="16" rx="3" fill="#fff"/><path d="M5 3.5l2 2-1 1.2a6 6 0 0 0 3.3 3.3l1.2-1 2 2-1.3 1.5C8 12.5 3.5 8 4 4.8z" fill="#111"/></svg>
          (623) 587-2914
        </li>
        <li>
          <svg viewBox="0 0 16 16" aria-hidden="true"><rect width="16" height="16" rx="3" fill="#fff"/><rect x="3" y="4.5" width="10" height="7" fill="none" stroke="#111" stroke-width="1.2"/><path d="M3 4.5l5 4 5-4" fill="none" stroke="#111" stroke-width="1.2"/></svg>
          info@markdorsey.com
        </li>
        <li>
          <svg viewBox="0 0 16 16" aria-hidden="true"><rect width="16" height="16" rx="3" fill="#fff"/><circle cx="8" cy="8" r="4.6" fill="none" stroke="#111" stroke-width="1.2"/><path d="M3.4 8h9.2M8 3.4c-2 2.6-2 6.6 0 9.2M8 3.4c2 2.6 2 6.6 0 9.2" fill="none" stroke="#111" stroke-width="1"/></svg>
          www.MarkDorsey.com
        </li>
      </ul>
      <address class="address">
        31872 W. Cedar Hollow Blvd.<br>
        Suite 207-418<br>
        Sunridge, Arizona 85390
      </address>
    </div>
  </section>
</body>
</html>
```